We need a need two-page flyer that talks about the services of Harbor Linkage. We like this created in ppt if possible (let me know if not). We have created the HL ppt for your reference. Please use the attached Oldharbor .pdf for reference. We like this to be fun and creative in flair and style. Something that the sales people can use and will wow the client if we email it to them.

```html
<!DOCTYPE html>
<html lang="en">
<head>
<meta charset="utf-8">
<title>Harbor Linkage – Two-Page Flyer</title>
<link href="https://fonts.googleapis.com/css2?family=Roboto+Condensed:wght@400;700&family=Roboto:wght@400;500&display=swap" rel="stylesheet">
<style>
  :root {
    --stage: #4a4a4c;
    --royal: #3f53b0;
    --royal-light: #5a6cc6;
    --lavender: #dfe1f2;
    --lavender-soft: #eef0f9;
    --ink: #222226;
    --charcoal: #201e1f;
    --white: #ffffff;
    --brand-red: #e03a2f;
    --brand-green: #56b146;
    --brand-blue: #3350a8;
    --grey-text: #5a5a60;
  }
  * { box-sizing: border-box; margin: 0; padding: 0; }
  html, body { width: 1200px; height: 1200px; overflow: hidden; }
  body {
    background: var(--stage);
    font-family: "Roboto", Arial, sans-serif;
    color: var(--ink);
    position: relative;
  }
  .page {
    position: absolute;
    width: 552px;
    height: 712px;
    background: var(--white);
    overflow: hidden;
  }
  .page--approach { left: 46px; top: 64px; }
  .page--services { left: 624px; top: 420px; }
  .abs { position: absolute; }
  .heading { font-family: "Roboto Condensed", Arial, sans-serif; }
  .copy { font-size: 8px; line-height: 10.8px; text-align: justify; }
  .copy p + p { margin-top: 8px; }
  .footer {
    position: absolute; left: 0; right: 0; bottom: 0; height: 44px;
    background: var(--charcoal); color: var(--white);
    font-size: 12px; letter-spacing: 3.2px;
    display: flex; align-items: center; justify-content: center;
  }

  /* Approach page */
  .approach-band {
    left: 0; top: 0; width: 100%; height: 82px;
    background: linear-gradient(180deg, var(--royal-light), var(--royal));
    color: var(--white); text-align: center;
  }
  .approach-band .kicker { font-family: "Roboto Condensed", sans-serif; font-size: 12.5px; margin-top: 23px; }
  .approach-band .title { font-family: "Roboto Condensed", sans-serif; font-weight: 700; font-size: 27px; line-height: 30px; }
  .approach-body {
    left: 0; top: 82px; width: 100%; height: 323px;
    background: linear-gradient(180deg, var(--lavender) 0%, var(--lavender-soft) 55%, var(--white) 100%);
  }
  .section-title { font-size: 14.5px; font-weight: 400; color: var(--ink); }
  .photo { position: absolute; }
  .photo--ship { left: 24px; top: 405px; width: 251px; height: 166px; background: linear-gradient(160deg, #3d6a98, #1f3b55 60%, #2f5a3c); }
  .photo--hangar { left: 277px; top: 405px; width: 250px; height: 166px; background: linear-gradient(180deg, #141414, #6a4a2a 55%, #c9c3bb); }
  .photo--stage { left: 24px; top: 574px; width: 503px; height: 92px; background: linear-gradient(90deg, #3a1048, #a23db8 45%, #5c1a70); }
  .photo-caption {
    left: 277px; top: 420px; width: 250px; text-align: center;
    font-family: "Roboto Condensed", sans-serif; font-size: 13.5px; color: var(--white);
  }

  /* Services page */
  .services-cap { left: 0; top: 0; width: 100%; height: 29px; background: var(--charcoal); }
  .brand-block { left: 0; top: 29px; width: 100%; height: 104px; background: var(--white); }
  .brand-name {
    left: 40px; top: 68px; display: flex; align-items: center; gap: 10px;
    font-family: "Roboto Condensed", sans-serif; font-size: 27px; color: var(--ink);
  }
  .brand-name .mark { width: 16px; height: 16px; background: var(--brand-blue); }
  .brand-divider { left: 278px; top: 46px; width: 1px; height: 76px; background: #b8b8c0; }
  .founded { left: 289px; top: 51px; width: 240px; font-size: 10px; line-height: 12px; color: var(--ink); }
  .photo--gala { left: 0; top: 133px; width: 100%; height: 205px; background: linear-gradient(180deg, #1d1a4a, #4a49a8 45%, #8c8fc9 75%, #2a2840); }
  .gala-caption {
    left: 0; top: 284px; width: 100%; height: 54px;
    background: rgba(20, 18, 40, 0.55); color: var(--white); text-align: center;
    font-family: "Roboto Condensed", sans-serif;
  }
  .gala-caption .main { font-size: 22px; line-height: 24px; margin-top: 4px; }
  .gala-caption .sub { font-size: 14px; line-height: 18px; letter-spacing: 0.3px; }
  .services-body {
    left: 0; top: 338px; width: 100%; height: 330px;
    background: linear-gradient(180deg, var(--lavender) 0%, var(--lavender-soft) 60%, var(--white) 100%);
  }
  .service-head { display: flex; align-items: center; gap: 8px; height: 40px; }
  .service-icon { width: 34px; height: 34px; border-radius: 6px; flex: none; }
  .service-title { font-family: "Roboto Condensed", sans-serif; font-weight: 700; font-size: 10.5px; line-height: 12.5px; color: var(--ink); }
  .service .copy { font-size: 7px; line-height: 9.6px; margin-top: 10px; }
  .service .copy p + p { margin-top: 7px; }
  .icon--props { background: linear-gradient(135deg, var(--brand-red), #7b2a8a); }
  .icon--led { background: radial-gradient(circle, #5ab9e6 40%, var(--brand-red) 42%); border-radius: 50%; }
  .icon--foliage { background: linear-gradient(180deg, #8fc25a, #3f7a2e); }
  .icon--ice { background: linear-gradient(135deg, #c8ecfb, #6cc4ea); }
  .icon--fab { background: radial-gradient(circle, #6b1a1a 30%, #2a2a2a 60%); border-radius: 50%; }
  .photo--foliage { left: 369px; top: 478px; width: 161px; height: 176px; background: linear-gradient(180deg, #2e6a2a, #7bb24e 50%, #4a3a2a); }
</style>
</head>
<body>

<section class="page page--approach">
  <header class="abs approach-band">
    <p class="kicker">PLAN YOUR NEXT EVENT NOW!</p>
    <h1 class="title">Our Approach to a Successful Event</h1>
  </header>
  <div class="abs approach-body"></div>

  <h2 class="abs heading section-title" style="left:37px; top:109px;">An Extension of Your Own team</h2>
  <div class="abs copy" style="left:37px; top:136px; width:493px;">
    <p>When you employ Harbor Linkage to create or manage one of your events, you can be assured that you are in the safe hands of thoroughbred event organizers.</p>
    <p>We like to work as an extension of your own company, treating your events and brands as respectfully as we do our own and consulting carefully on all significant decisions.</p>
    <p>We have a strong understanding of budget constraints, constantly monitoring expenditure commitments and managing the various risks involved.</p>
    <p>We use our extensive supplier and venue relationships to keep your costs low whilst ensuring the highest quality, with many clients finding that using our services is more cost-effective than running their events through an in-house team.</p>
  </div>

  <h2 class="abs heading section-title" style="left:36px; top:280px;">Budget transparency</h2>
  <div class="abs copy" style="left:36px; top:305px; width:223px;">
    <p>We always work to a pre-agreed budget and a pre-agreed management fee, based on the amount of sales, marketing and logistical time needed to manage your event.</p>
    <p>Your final bill will not differ from this pre-agreed amount unless there have been significant changes to the project along the way.</p>
  </div>

  <h2 class="abs heading section-title" style="left:284px; top:280px;">Meet the team</h2>
  <div class="abs copy" style="left:284px; top:305px; width:243px;">
    <p>Organizing professional events requires a significant amount of time and ‘attention-to-detail’ across a whole range of different disciplines – but we endeavor to provide a single point of contact to streamline client communications wherever possible.</p>
  </div>

  <div class="photo photo--ship" role="img" aria-label="Photo of a themed shipwreck stage set with a ship's wheel under blue and green lighting"></div>
  <div class="photo photo--hangar" role="img" aria-label="Photo of a banquet set up beneath vintage aircraft in a hangar"></div>
  <p class="abs photo-caption">Creating the Ultimate Event Experience</p>
  <div class="photo photo--stage" role="img" aria-label="Photo of a concert stage with a drum kit under purple lighting"></div>

  <footer class="footer">www.harborlinkage.com</footer>
</section>

<section class="page page--services">
  <div class="abs services-cap"></div>
  <div class="abs brand-block"></div>
  <div class="abs brand-name"><span class="mark"></span><span>Harbor Linkage</span></div>
  <div class="abs brand-divider"></div>
  <p class="abs founded">Founded in 1999,<br>Harbor Linkage is a specialist organizer of business-to-business events, including conferences, award ceremonies, seminars, workshops, roadshows, roundtables and exhibitions for the public, commercial and third sectors.</p>

  <div class="photo photo--gala" role="img" aria-label="Photo of a large ballroom with dressed round tables under blue lighting"></div>
  <div class="abs gala-caption">
    <p class="main">Event Management Services</p>
    <p class="sub">BRINGING PEOPLE, BUSINESSES, MARKETS AND IDEAS TOGETHER</p>
  </div>

  <div class="abs services-body"></div>

  <article class="abs service" style="left:28px; top:352px; width:160px;">
    <div class="service-head"><div class="service-icon icon--props" role="img" aria-label="Masquerade mask icon"></div><h3 class="service-title">Themed Props<br>and Décor</h3></div>
    <div class="copy">
      <p>At Harbor Linkage we are known for providing décor that completely changes the surrounds of your venue and provides your guests with an immersive event experience. Our expert event designers understand how the product will be used and where it will be most impactful.</p>
      <p>Whether being transported to outer space or to a tropical paradise, our props drive each theme home. We also will use foliage, lighting, ice, and even custom décor items</p>
    </div>
  </article>

  <article class="abs service" style="left:200px; top:352px; width:160px;">
    <div class="service-head"><div class="service-icon icon--led" role="img" aria-label="Light bulb ring icon"></div><h3 class="service-title">LED<br>Glow Linkage</h3></div>
    <div class="copy">
      <p>Glow Linkage was born from the need to eliminate pesky cords at our events. Our lighted décor is now completely battery operated. We now sell most of our lights to multiple companies and theme parks throughout the United States.</p>
      <p>Our lighted products are brand friendly, meaning we can add a logo or monogram to just about any of our lighted décor items.</p>
    </div>
  </article>

  <article class="abs service" style="left:368px; top:352px; width:162px;">
    <div class="service-head"><div class="service-icon icon--foliage" role="img" aria-label="Palm plant icon"></div><h3 class="service-title">Foliage<br>Greenery Linkage</h3></div>
    <div class="copy">
      <p>Greenery Linkage is our only company that is not located on property.</p>
      <p>We have 40,000 square feet of green houses with a large selection of inventory from 14’ Amstel Ficus Trees, 12’ Palms, to lush Boston Ferns and many more in between.</p>
    </div>
  </article>
  <div class="photo photo--foliage" role="img" aria-label="Photo of a tropical palm arrangement with a carved tiki statue"></div>

  <article class="abs service" style="left:34px; top:522px; width:158px;">
    <div class="service-head"><div class="service-icon icon--ice" role="img" aria-label="Ice cube icon"></div><h3 class="service-title">Carving<br>Ice</h3></div>
    <div class="copy">
      <p>Ice sculptures are a central point and unique statement at a corporate event or wedding. Ice will attract attention and provide a memorable focal and visual for attendee discussion.</p>
      <p>It can even be an interactive experience when your guests use an ice luge for the first time or drink from a glass with a large ice cube featuring your logo!</p>
    </div>
  </article>

  <article class="abs service" style="left:202px; top:522px; width:158px;">
    <div class="service-head"><div class="service-icon icon--fab" role="img" aria-label="Saw blade icon"></div><h3 class="service-title">Custom Fabrication for<br>All Types of Events</h3></div>
    <div class="copy">
      <p>At Harbor Linkage our in-house fabrication team has the ability to deliver custom designs and fabrications that will make your next event a unique one. Our team of professionals specializes in providing creative event solutions for companies planning both in-office and off-site activities. Our services provide the very best in custom staging, furniture and décor, scenic displays, tradeshow booths, and much more.</p>
    </div>
  </article>

  <footer class="footer">www.harborlinkage.com</footer>
</section>

</body>
</html>
```